House Builder and Property Development Card Design and Logo

I need a business card design for a building and property development company.
Colour scheme of Dark Grey and Green, I would like it bold, sharp and professional.
No logo yet done, I'm open to options but please stay away from the usual- house, roof, hammers etc.
Thanks Rob

Please be aware that on the business card information section the WHRC # 5528391 is a licence number and my phone number 0492837165. The numbers are close together and could be mistaken as one whole number 

Thank you

                                   

Industry/Entity Type

Building

Contact Information for Business Card

VARGA BUILD & DEVELOPMENT.
Residential Building & Property Development
Robert Varga - Director
WHRC # 5528391
0492837165
rob@vargabuild.example.com.au

Requirements
Must have
• Bold Business name
Dark grey and green colours
Should not have
• roof outline or hammer logo

```html
<!DOCTYPE html>
<html lang="en">
<head>
<meta charset="utf-8">
<title>Varga Build &amp; Development – Business Card</title>
<link rel="stylesheet" href="https://fonts.googleapis.com/css2?family=Russo+One&family=Arimo:wght@400;700&display=swap">
<style>
  :root {
    --page: #e9e9e7;
    --charcoal: #4b4b4b;
    --charcoal-deep: #3c3c3c;
    --ink: #1f1f1f;
    --paper: #f7f7f7;
    --paper-shade: #e6e6e6;
    --green: #7dbb3c;
    --white: #ffffff;
    --rule: #2a2a2a;
  }
  * { box-sizing: border-box; margin: 0; padding: 0; }
  html, body {
    width: 1200px; height: 995px; overflow: hidden;
    background: var(--page);
  }
  .canvas { position: relative; width: 1200px; height: 995px; }

  .card {
    position: absolute; width: 700px; height: 428px; overflow: hidden;
    box-shadow: 0 6px 18px rgba(0,0,0,.18);
  }
  .card--back {
    left: 80px; top: 40px;
    background: radial-gradient(ellipse at 55% 35%, #5c5c5c 0%, var(--charcoal) 55%, var(--charcoal-deep) 100%);
  }
  .card--front {
    left: 420px; top: 520px;
    background: radial-gradient(ellipse at 45% 40%, var(--white) 0%, var(--paper) 55%, var(--paper-shade) 100%);
  }

  .brand {
    position: absolute; left: 0; right: 0;
    display: flex; align-items: center; justify-content: center; gap: 14px;
    font-family: "Russo One", sans-serif;
  }
  .brand__mark { width: 34px; height: 34px; background: var(--green); flex: none; }
  .brand__name { font-size: 34px; letter-spacing: .5px; }
  .card--back .brand { top: 140px; }
  .card--back .brand__name { color: var(--white); }
  .card--front .brand { top: 48px; }
  .card--front .brand__name { color: var(--ink); font-size: 30px; }
  .card--front .brand__mark { width: 30px; height: 30px; }

  .tagline {
    position: absolute; left: 0; right: 0; text-align: center;
    font-family: "Russo One", sans-serif;
  }
  .card--back .tagline { top: 206px; color: var(--white); font-size: 24px; }
  .card--front .tagline { top: 104px; color: var(--ink); font-size: 17px; }

  .person { position: absolute; top: 150px; left: 0; right: 0; text-align: center; font-family: "Arimo", sans-serif; }
  .person__name { color: var(--green); font-weight: 700; font-size: 22px; }
  .person__role { color: var(--ink); font-size: 17px; margin-top: 2px; }

  .rule { position: absolute; height: 2px; background: var(--rule); }
  .rule--left { left: 60px; width: 240px; top: 176px; }
  .rule--right { left: 470px; width: 230px; top: 226px; }

  .contact {
    position: absolute; top: 252px; left: 0; right: 0;
    font-family: "Arimo", sans-serif; font-size: 15px; letter-spacing: 1.5px; color: var(--ink);
    list-style: none; text-align: center;
  }
  .contact li { display: flex; align-items: center; justify-content: center; gap: 8px; height: 26px; }
  .contact svg { flex: none; }

  .bands { position: absolute; left: 0; bottom: 0; }
</style>
</head>
<body>
<main class="canvas">

  <section class="card card--back" aria-label="Card back">
    <div class="brand">
      <span class="brand__mark"></span>
      <span class="brand__name">VARGA BUILD &amp; DEVELOPMENT</span>
    </div>
    <p class="tagline">Residential Building &amp; Property Development</p>
  </section>

  <section class="card card--front" aria-label="Card front">
    <div class="brand">
      <span class="brand__mark"></span>
      <span class="brand__name">VARGA BUILD &amp; DEVELOPMENT</span>
    </div>
    <p class="tagline">Residential Building &amp; Property Development</p>

    <div class="rule rule--left"></div>
    <div class="person">
      <p class="person__name">Robert Varga</p>
      <p class="person__role">Director</p>
    </div>
    <div class="rule rule--right"></div>

    <ul class="contact">
      <li>
        <svg width="12" height="18" viewBox="0 0 12 18" aria-hidden="true">
          <rect x="1" y="1" width="10" height="16" rx="2" fill="none" stroke="var(--green)" stroke-width="1.6"/>
          <line x1="4" y1="14" x2="8" y2="14" stroke="var(--green)" stroke-width="1.4"/>
        </svg>
        <span>0492837165</span>
      </li>
      <li>
        <svg width="20" height="14" viewBox="0 0 20 14" aria-hidden="true">
          <rect x="0" y="0" width="20" height="14" fill="var(--green)"/>
          <polyline points="0,0 10,8 20,0" fill="none" stroke="var(--white)" stroke-width="1.4"/>
        </svg>
        <span>rob@vargabuild.example.com.au</span>
      </li>
      <li><span>WHRC # 5528391</span></li>
    </ul>

    <svg class="bands" width="700" height="100" viewBox="0 0 700 100" aria-hidden="true">
      <polygon points="0,10 430,10 410,34 0,34" fill="var(--charcoal)"/>
      <polygon points="410,40 700,40 700,90 372,90" fill="var(--green)"/>
    </svg>
  </section>

</main>
</body>
</html>
```